依頼詳細
・リスティングでの運用を考えているので、コンバージョンを期待できるデザイン、サイト構成
・レスポンシブでコーディングするためそれを念頭に置いたデザイン
・提案デザインはスマホ、PC両画面でお願いします。
・サイト構成も変わる可能性が高いので、HTMLやCSSでの変更が容易なデザイン
(メニューなどを画像にしないetc)
・奇抜さよりも安心感
・病院関係のウェブサイト構築実績のある方歓迎
・病院の場所はみなとみらいです。
ページ数
2ページ
希望イメージ
シンプル 複雑
単色 カラフル
暗い 明るい
日常 高級
遊び心 厳粛
未来的 伝統的
女性的 男性的
希望する色
青系、水色系、緑系、黄・オレンジ系
納品ファイル
• 高解像度JPG (.jpg)
• フォトショップ形式 (.psd)
補足説明
■ 補足
--------------------------------
・基本HTMLコーディングは無しで構いませんが、
対応可能な方はコーディング作業についてもお見積ください。

・採用された方は今後も引続き作業をお願いすることになると思います。

■ 注意点

・お渡しできる素材は、サイトマップのみとなります
・病院名なども決まっていないので、ロゴなどは仮のもので構いません。
・サイトの中の文言なども仮の文章で構いません。
・写真素材も仮のもので構いません。
(最終的には素材もしくは撮影した写真に入れ替えます。)

○想定サイトマップ
診療科目
病院案内
├ ご挨拶・理念
├ 施設案内
└ ドクター紹介
アクセス
よくある質問
採用情報
サイトマップ
お問い合わせ
予約

※サイト構成も決定ではないので提案頂く形でも構いません。

参考サイト
http://www.hizuki-dental.com/
https://www.clinic-kotobe.com/
ウェブサイトの構成が、内科・整形外科・歯科の診療科目を一つのサイトで集患する形に変更になりました。大きい枠組みで変わるのはこれ以降はないと思います。素敵なデザイナー様との出会いを期待しております。
お盆に入ってしまうので、締切を延長させていただきました。今後も数々の案件抱えておりますので、長いお付き合いができるデザイナー様との出会いを期待しております。
たくさんのご応募、誠にありがとうございます!

これから社内で選定を行います。
一週間以内には決定できると思いますので少々お待ち頂ければと思います。
よろしくお願いいたします。
デザインの選定に時間がかかっておりますので、決定までもう少々お待ち頂ければと思います。申し訳ありません、よろしくお願いいたします。
■ 選んだ理由

シンプルにデザインがまとまっていたところと、アイコンなどを使いぱっと見た時のわかりやすさ、写真を変更しても違和感なくマッチしそうな点などを評価させていただきました。

■ 提案者全員のお礼・コメント

この度は弊社コンペにご参加頂き誠にありがとうございます。
優れたデザイン・提案を多数頂きとても感謝しております。

ギリギリまでどの提案を採用させていただくか迷いましたが、
今回はこのような結果となりました。

またの機会がありましたら、またぜひご参加頂ければ幸いです。
ありがとうございました。

```html
<!DOCTYPE html>
<html lang="ja">
<head>
<meta charset="utf-8">
<title>ハーバー内科・整形外科</title>
<link href="https://fonts.googleapis.com/css2?family=Noto+Sans+JP:wght@400;500;700&family=Noto+Serif+JP:wght@400;500&display=swap" rel="stylesheet">
<style>
:root{
  --bg-outer:#ffffff;
  --bg-frame:#ece5d5;
  --page:#ffffff;
  --teal:#4fb6c8;
  --teal-dark:#2f9bb0;
  --teal-pale:#bfe3ea;
  --text:#4a4a4a;
  --muted:#8a8a8a;
  --brown:#8a6a4a;
}
*{box-sizing:border-box;margin:0;padding:0}
html,body{width:1200px;height:2280px;overflow:hidden;background:var(--bg-outer)}
body{font-family:"Noto Sans JP",sans-serif;color:var(--text);position:relative}
.frame{position:absolute;left:160px;top:232px;width:900px;height:1830px;background:var(--bg-frame)}
.page{position:absolute;left:260px;top:232px;width:720px;height:1716px;background:var(--page)}
.site-footer{position:absolute;left:160px;top:1948px;width:900px;height:100px;background:var(--teal-pale);
  display:flex;align-items:center;justify-content:center;font-size:14px;color:var(--teal-dark);font-family:"Noto Serif JP",serif}

/* header */
.site-header{position:absolute;left:40px;top:24px;width:640px;height:70px}
.brand{position:absolute;left:0;top:4px;display:flex;align-items:center;gap:14px}
.brand-mark{width:50px;height:50px;background:var(--teal);flex:none}
.brand-name{font-family:"Noto Serif JP",serif;font-size:22px;color:var(--text);line-height:1.2;white-space:nowrap}
.brand-sub{display:block;font-size:13px;color:var(--muted);letter-spacing:.05em}
.contact{position:absolute;right:0;top:4px;text-align:right}
.contact-tel{display:flex;align-items:center;justify-content:flex-end;gap:8px;font-size:26px;font-weight:700;color:var(--text);letter-spacing:.02em;line-height:1.3}
.contact-note{font-size:11px;color:var(--muted);margin-top:2px}

.global-nav{position:absolute;left:40px;top:150px;width:640px;display:flex;gap:14px;font-size:13px;color:var(--teal-dark)}

/* hero */
.hero{position:absolute;left:40px;top:176px;width:640px;height:180px;background:linear-gradient(160deg,#f3f1ec 0%,#d9d6cf 45%,#b7a9a0 70%,#d2cfc7 100%)}
.hero-accent{position:absolute;right:0;top:14px;width:260px;height:70px;background:linear-gradient(90deg,#c94a44,#e0716a)}
.hero-title{position:absolute;left:14px;top:16px;background:rgba(79,182,200,.85);color:#fff;font-size:14px;padding:4px 10px}
.hero-caption{position:absolute;right:18px;bottom:18px;width:260px;background:rgba(255,255,255,.85);font-size:12px;line-height:1.8;padding:8px 12px;color:var(--text)}

/* sections */
.section-title{position:absolute;left:40px;width:640px;font-size:17px;font-weight:500;color:var(--teal-dark);padding-bottom:6px;border-bottom:2px solid var(--teal-pale)}
.btn{position:absolute;width:260px;height:48px;border:2px solid var(--teal);color:var(--teal-dark);font-size:14px;
  display:flex;align-items:center;justify-content:center;gap:10px;background:#fff}
.btn::before{content:"›";font-size:18px;line-height:1}

.about-photo{position:absolute;left:60px;top:470px;width:270px;height:200px;background:linear-gradient(180deg,#6d89b8 0%,#9fb3d4 45%,#e2e4e8 65%,#b7b9bd 100%)}
.about-text{position:absolute;left:370px;top:500px;width:300px;font-size:14px;line-height:2.1;color:var(--text)}

.depts{position:absolute;left:40px;top:790px;width:640px;display:flex;justify-content:space-between;padding:0 10px}
.dept{width:190px;text-align:center}
.dept-name{font-size:16px;color:var(--brown);font-weight:500;margin-bottom:8px}
.dept-photo{width:190px;height:150px}
.dept-photo.naika{background:linear-gradient(135deg,#f4f6f8,#c9d7e2)}
.dept-photo.seikei{background:linear-gradient(135deg,#fbf6ee,#e9d8c4)}
.dept-photo.shika{background:linear-gradient(135deg,#f8eee8,#e6cbbd)}

.access-name{position:absolute;left:50px;top:1168px;font-family:"Noto Serif JP",serif;font-size:19px}
.access-mark{position:absolute;left:130px;top:1210px;width:46px;height:46px;background:var(--teal)}
.access-address{position:absolute;left:50px;top:1280px;font-size:13px;line-height:1.7}
.map{position:absolute;left:370px;top:1160px;width:310px;height:230px;background:linear-gradient(135deg,#e9ecef,#d4dbe2 50%,#c9d3dc)}

.hours{position:absolute;left:80px;top:1440px;width:560px;border-collapse:collapse;font-size:12px;text-align:center}
.hours th{background:var(--teal);color:#fff;font-weight:500;height:28px;border:1px solid #fff}
.hours td{height:26px;border:1px solid #fff;background:#eef7f9;color:var(--text)}
.hours td.time{background:#e2f2f5;color:var(--teal-dark)}
.hours-note{position:absolute;left:80px;top:1530px;width:560px;font-size:11px;color:var(--teal-dark)}
</style>
</head>
<body>
<div class="frame"></div>
<div class="page">
  <header class="site-header">
    <div class="brand">
      <div class="brand-mark"></div>
      <div class="brand-name">ハーバー内科・整形外科<span class="brand-sub">harbor clinic</span></div>
    </div>
    <div class="contact">
      <div class="contact-tel">
        <svg width="22" height="22" viewBox="0 0 24 24"><path d="M6.6 10.8a15 15 0 0 0 6.6 6.6l2.2-2.2c.3-.3.7-.4 1-.2 1.1.4 2.3.6 3.6.6.6 0 1 .4 1 1V20c0 .6-.4 1-1 1A17 17 0 0 1 3 4c0-.6.4-1 1-1h3.5c.6 0 1 .4 1 1 0 1.3.2 2.5.6 3.6.1.3 0 .7-.2 1z" fill="#4a4a4a"/></svg>
        045-555-0123
      </div>
      <p class="contact-note">受付時間 平日9:00〜18:30 お気軽にお問い合わせください</p>
    </div>
  </header>

  <nav class="global-nav">
    <span>HOME</span><span>診療科目</span><span>病院案内</span><span>アクセス</span><span>よくある質問</span><span>採用情報</span><span>サイトマップ</span><span>お問い合わせ</span><span>予約</span>
  </nav>

  <div class="hero" role="img" aria-label="明るい待合室の写真">
    <div class="hero-accent"></div>
    <p class="hero-title">みなとみらい地区で選ばれる病院を目指して</p>
    <p class="hero-caption">ハーバー内科・整形外科は地域の皆様に安心の医療をお届けします。</p>
  </div>

  <h2 class="section-title" style="top:410px">病院案内</h2>
  <div class="about-photo" role="img" aria-label="青空と病院の外観の写真"></div>
  <p class="about-text">患者様の「安心」を最優先に<br>「あなたの身になって考える」<br>それをMOTTOに患者様に<br>寄り添った治療を提供いたします</p>
  <a class="btn" style="left:390px;top:640px">詳しくはこちら</a>

  <h2 class="section-title" style="top:742px">診療科目</h2>
  <div class="depts">
    <div class="dept"><p class="dept-name">内科</p><div class="dept-photo naika" role="img" aria-label="点滴と聴診器の写真"></div></div>
    <div class="dept"><p class="dept-name">整形外科</p><div class="dept-photo seikei" role="img" aria-label="背骨の模型の写真"></div></div>
    <div class="dept"><p class="dept-name">歯科</p><div class="dept-photo shika" role="img" aria-label="歯のケアの写真"></div></div>
  </div>
  <a class="btn" style="left:230px;top:1036px">診療内容</a>

  <h2 class="section-title" style="top:1112px">アクセスマップ</h2>
  <p class="access-name">ハーバー内科・整形外科</p>
  <div class="access-mark"></div>
  <p class="access-address">〒220-0000<br>神奈川県横浜市西区みなとみらい</p>
  <a class="btn" style="left:50px;top:1340px;width:240px">アクセス</a>
  <div class="map" role="img" aria-label="みなとみらい周辺の地図"></div>

  <table class="hours">
    <tr><th style="width:160px">診療時間</th><th>月</th><th>火</th><th>水</th><th>木</th><th>金</th><th>土</th><th>日</th></tr>
    <tr><td class="time">午前9:00〜12:00</td><td>○</td><td>○</td><td>○</td><td>○</td><td>○</td><td>○</td><td>／</td></tr>
    <tr><td class="time">午後15:00〜18:30</td><td>○</td><td>○</td><td>○</td><td>／</td><td>○</td><td>／</td><td>／</td></tr>
  </table>
  <p class="hours-note">診療時間／午前9:00〜12:00 午後15:00〜18:30　休診日／木・土午後、日祝</p>
</div>
<footer class="site-footer">Copyright© Harbor Clinic All Rights Reserved.</footer>
</body>
</html>
```